Poster Design for kebab shop products

need a new poster for our new velmo pack special, sign will be inside of shopping centre at different location to shop will need to stand out and draw customers to the store, MUST contain shops logo & picture added, poster size will be 76cm x 101cm so will need to suit that size

MUST ALSO CONTAIN THE FOLLOWING
Velmo Pack / HSP
Lamb & Chips
Chicken & Chips
Beef & Chips
+ Can $15

Target Market(s)

new customers

Industry/Entity Type

Retail

Font styles to use
Sans Serif

Colors

Designer to choose colors to be used in the design.

Requirements
Must have
• company logo
• picture of vemo pack provided
• Velmo Pack / HSP
• Lamb & Chips
• Chicken & Chips
• Beef & Chips
• + Can $15

```html
<!DOCTYPE html>
<html lang="en">
<head>
<meta charset="utf-8">
<title>Velmo Pack Special</title>
<link rel="stylesheet" href="https://fonts.googleapis.com/css2?family=Archivo+Black&family=Oswald:wght@600;700&display=swap">
<style>
  :root {
    --red-core: #c4121f;
    --red-mid: #8e0a12;
    --red-deep: #4e0307;
    --cream: #fdebc4;
    --cream-light: #fff7e2;
    --white: #ffffff;
    --ink: #111111;
    --yellow: #ffd21a;
    --yellow-deep: #f5a800;
    --orange: #f08a00;
    --badge-red: #d4121c;
    --shadow: rgba(40, 0, 0, 0.65);
  }
  * { margin: 0; padding: 0; box-sizing: border-box; }
  html, body { width: 776px; height: 1200px; overflow: hidden; background: var(--red-deep); }
  .poster {
    position: relative;
    width: 776px;
    height: 1200px;
    overflow: hidden;
    background: radial-gradient(ellipse 70% 55% at 50% 42%, var(--red-core) 0%, var(--red-mid) 55%, var(--red-deep) 100%);
    font-family: "Archivo Black", sans-serif;
  }
  .brand-plate {
    position: absolute;
    left: 264px;
    top: 0;
    width: 282px;
    height: 150px;
    background: linear-gradient(180deg, var(--cream-light), var(--cream));
    clip-path: polygon(0 0, 100% 0, 100% 83%, 56% 83%, 50% 100%, 44% 83%, 0 83%);
    display: flex;
    align-items: center;
    justify-content: center;
    padding-bottom: 26px;
  }
  .brand-name {
    font-family: "Oswald", sans-serif;
    font-weight: 700;
    font-size: 34px;
    letter-spacing: 1px;
    color: var(--badge-red);
    text-transform: uppercase;
  }
  .headline {
    position: absolute;
    left: 0;
    right: 0;
    top: 168px;
    text-align: center;
    color: var(--white);
    font-size: 128px;
    line-height: 128px;
    letter-spacing: -2px;
    text-transform: uppercase;
    text-shadow: 0 6px 0 #d9d9d9, 0 10px 14px var(--shadow);
  }
  .headline span { display: block; }
  .headline span + span { margin-top: 8px; }
  .product-photo {
    position: absolute;
    left: 113px;
    top: 470px;
    width: 534px;
    height: 480px;
    border-radius: 22px;
    background: radial-gradient(ellipse 60% 45% at 50% 58%, #7a4a2c 0%, #b58a4a 45%, #e9dfc9 75%, #f6f4ef 100%);
  }
  .special-tag {
    position: absolute;
    left: 487px;
    top: 504px;
    width: 190px;
    height: 100px;
  }
  .special-tag .tag-shadow {
    position: absolute;
    left: 6px;
    top: 22px;
    width: 170px;
    height: 74px;
    background: var(--badge-red);
    transform: skewY(-6deg);
  }
  .special-tag .tag-face {
    position: absolute;
    left: 0;
    top: 6px;
    width: 176px;
    height: 76px;
    background: var(--yellow);
    transform: skewY(-6deg);
    display: flex;
    align-items: center;
    justify-content: center;
  }
  .special-tag .tag-label {
    font-family: "Oswald", sans-serif;
    font-weight: 700;
    font-size: 40px;
    color: var(--ink);
    letter-spacing: 0.5px;
  }
  .price-burst {
    position: absolute;
    left: 122px;
    top: 988px;
    width: 172px;
    height: 172px;
  }
  .price-burst svg { position: absolute; inset: 0; }
  .price-amount {
    position: absolute;
    inset: 0;
    display: flex;
    align-items: center;
    justify-content: center;
    font-family: "Oswald", sans-serif;
    font-weight: 700;
    font-size: 68px;
    color: var(--ink);
    font-style: italic;
    letter-spacing: -1px;
  }
  .price-amount sup { font-size: 36px; margin-top: -18px; }
  .pack-options {
    position: absolute;
    left: 306px;
    top: 1006px;
    list-style: none;
    font-family: "Oswald", sans-serif;
    font-weight: 600;
    font-size: 27px;
    line-height: 36px;
    color: var(--white);
    text-transform: uppercase;
    letter-spacing: 0.3px;
  }
  .pack-options li { display: flex; align-items: center; gap: 10px; }
  .pack-options .arrow { width: 14px; height: 16px; flex: none; }
  .pack-options .extra { padding-left: 24px; }
</style>
</head>
<body>
  <main class="poster">
    <header class="brand-plate">
      <span class="brand-name">Spit Harbour</span>
    </header>

    <h1 class="headline"><span>Velmo</span><span>Pack</span></h1>

    <div class="product-photo" role="img" aria-label="Open takeaway box of chips topped with sliced kebab meat, garlic sauce and chilli sauce"></div>

    <div class="special-tag">
      <div class="tag-shadow"></div>
      <div class="tag-face"><span class="tag-label">SPECIAL</span></div>
    </div>

    <div class="price-burst">
      <svg viewBox="0 0 172 172" width="172" height="172" aria-hidden="true">
        <g fill="var(--yellow)" stroke="var(--yellow-deep)" stroke-width="2">
          <rect x="27" y="27" width="118" height="118" transform="rotate(0 86 86)"/>
          <rect x="27" y="27" width="118" height="118" transform="rotate(22.5 86 86)"/>
          <rect x="27" y="27" width="118" height="118" transform="rotate(45 86 86)"/>
          <rect x="27" y="27" width="118" height="118" transform="rotate(67.5 86 86)"/>
        </g>
        <circle cx="86" cy="86" r="62" fill="var(--yellow)"/>
      </svg>
      <div class="price-amount"><sup>$</sup>15</div>
    </div>

    <ul class="pack-options">
      <li><svg class="arrow" viewBox="0 0 14 16"><polygon points="0,0 14,8 0,16 4,8" fill="var(--orange)"/></svg>Lamb &amp; Chips</li>
      <li><svg class="arrow" viewBox="0 0 14 16"><polygon points="0,0 14,8 0,16 4,8" fill="var(--orange)"/></svg>Chicken &amp; Chips</li>
      <li><svg class="arrow" viewBox="0 0 14 16"><polygon points="0,0 14,8 0,16 4,8" fill="var(--orange)"/></svg>Beef &amp; Chips</li>
      <li class="extra">+ Can</li>
    </ul>
  </main>
</body>
</html>
```